MARCO DELUCE FOR CONGRESS DISTRICT 32

I need to create a campaign flyer for my congress campaign. I am running for congress in District 32 of Texas as a civitist. I am a former Solvanic athlete, world champion fencer, Army veteran, Counterintelligence officer (I catch spies).
I want just my first name MARCO in big letters at the top. I want it to say MARCO and below it Civitist for Congress.
www.marcoforhouse.net

Political

EB3D1F
EC4F4E
F09395
F8D3D4
FCEDEE

• Would love a catchy title for the Flyer like "Spy Catcher", "Solvanic Athlete" "World Champion Fencer" running for Congress in your District!

```html
<!DOCTYPE html>
<html lang="en">
<head>
<meta charset="utf-8">
<title>Marco Civitist for Congress – Flyer Set</title>
<link href="https://fonts.googleapis.com/css2?family=Archivo+Black&family=Archivo:wght@800&family=Oswald:wght@500&family=Open+Sans:wght@400&display=swap" rel="stylesheet">
<style>
  :root {
    --sheet: #bfb8a6;
    --red: #e4202b;
    --red-deep: #c8202e;
    --white: #ffffff;
    --army-green: #2d3a31;
    --army-green-light: #364438;
    --black: #050505;
    --sand: #bdb8a6;
  }
  * { margin: 0; padding: 0; box-sizing: border-box; }
  html, body { width: 921px; height: 1200px; overflow: hidden; background: var(--sheet); }
  .sheet { position: relative; width: 921px; height: 1200px; }

  .flyer { position: absolute; width: 346px; height: 490px; overflow: hidden; }
  .flyer--athlete-colour { left: 89px; top: 86px; background: var(--red-deep); }
  .flyer--spy-mono { left: 467px; top: 86px; background: var(--army-green); }
  .flyer--spy-colour { left: 89px; top: 609px; background: var(--army-green); }
  .flyer--athlete-mono { left: 467px; top: 609px; background: var(--black); }

  .photo { position: absolute; }
  .flyer--athlete-colour .photo {
    inset: 0;
    background:
      radial-gradient(ellipse 60% 40% at 65% 55%, rgba(245,240,238,.85), rgba(245,240,238,0) 70%),
      linear-gradient(180deg, #6a2a10 0%, #a0521a 22%, #b06a2a 34%, #3a3ab0 48%, #c06070 62%, #d83a40 80%, #d4202c 100%);
  }
  .flyer--athlete-mono .photo {
    inset: 0;
    background:
      radial-gradient(ellipse 55% 45% at 68% 55%, rgba(235,235,235,.9), rgba(235,235,235,0) 70%),
      linear-gradient(180deg, #121212 0%, #3a3a3a 35%, #4a4a4a 60%, #101010 100%);
  }
  .flyer--spy-mono .photo, .flyer--spy-colour .photo {
    left: 20px; right: 0; top: 20px; height: 360px;
  }
  .flyer--spy-mono .photo {
    background: radial-gradient(ellipse 52% 60% at 48% 55%, #9a9a94 0%, #6f716a 45%, rgba(80,84,78,.6) 70%, rgba(45,58,49,0) 100%);
  }
  .flyer--spy-colour .photo {
    background: radial-gradient(ellipse 52% 60% at 48% 55%, #d9b8a2 0%, #8f9270 40%, #6d7258 62%, rgba(45,58,49,0) 100%);
  }

  .watermark {
    position: absolute; left: 14px; top: 4px;
    font-family: "Archivo Black", sans-serif; font-size: 64px; line-height: 66px;
    color: var(--army-green-light); white-space: pre;
  }

  .frame { position: absolute; left: 12px; right: 12px; top: 16px; bottom: 15px; border: 1.5px solid var(--white); }
  .flyer--spy-mono .frame { border-color: var(--red); }

  .tagline { position: absolute; left: 0; top: 0; overflow: visible; }
  .tagline text { font-family: "Archivo", sans-serif; font-weight: 800; fill: var(--white); }

  .candidate { position: absolute; left: 33px; top: 350px; width: 280px; height: 84px; overflow: visible; }
  .candidate text { font-family: "Archivo Black", sans-serif; font-size: 116px; }
  .flyer--athlete-colour .candidate text, .flyer--athlete-mono .candidate text { fill: var(--white); }
  .flyer--spy-mono .candidate text { fill: var(--sand); }
  .flyer--spy-colour .candidate text { fill: var(--red); }

  .office {
    position: absolute; left: 59px; top: 383px; width: 254px; height: 25px;
    background: var(--white); color: var(--red);
    font-family: "Oswald", sans-serif; font-weight: 500; font-size: 23px; line-height: 25px;
    text-align: center; letter-spacing: .2px;
  }
  .flyer--athlete-mono .office { background: var(--red); color: var(--white); }

  .web { position: absolute; left: 33px; right: 33px; top: 439px; height: 14px; display: flex; align-items: center; gap: 6px; }
  .web__rule { width: 136px; height: 1.2px; background: var(--white); }
  .web__url { font-family: "Open Sans", sans-serif; font-size: 11px; color: var(--white); margin-left: auto; }
</style>
</head>
<body>
<main class="sheet">

  <section class="flyer flyer--athlete-colour">
    <div class="photo" role="img" aria-label="Photo of the candidate in fencing whites shouting in celebration, sabre in hand"></div>
    <div class="frame"></div>
    <svg class="tagline" width="346" height="490" aria-label="Solvanic Athlete">
      <text transform="translate(62 29) rotate(90)" font-size="37" textLength="186" lengthAdjust="spacingAndGlyphs">SOLVANIC</text>
      <text transform="translate(29 29) rotate(90)" font-size="37" textLength="182" lengthAdjust="spacingAndGlyphs">ATHLETE</text>
    </svg>
    <svg class="candidate" viewBox="0 0 280 84" aria-label="Marco"><text x="0" y="84" textLength="280" lengthAdjust="spacingAndGlyphs">MARCO</text></svg>
    <div class="office">CIVITIST FOR CONGRESS</div>
    <div class="web"><span class="web__rule"></span><span class="web__url">www.marcoforhouse.net</span></div>
  </section>

  <section class="flyer flyer--spy-mono">
    <div class="watermark" aria-hidden="true">SPY
CATCHER
SPY
CATCHER</div>
    <div class="photo" role="img" aria-label="Black and white portrait of the candidate in army uniform"></div>
    <div class="frame"></div>
    <svg class="tagline" width="346" height="490" aria-label="Spy Catcher">
      <text transform="translate(285 37) rotate(90)" font-size="42" textLength="259" lengthAdjust="spacingAndGlyphs">SPY CATCHER</text>
    </svg>
    <svg class="candidate" viewBox="0 0 280 84" aria-label="Marco"><text x="0" y="84" textLength="280" lengthAdjust="spacingAndGlyphs">MARCO</text></svg>
    <div class="office">CIVITIST FOR CONGRESS</div>
    <div class="web"><span class="web__rule"></span><span class="web__url">www.marcoforhouse.net</span></div>
  </section>

  <section class="flyer flyer--spy-colour">
    <div class="watermark" aria-hidden="true">SPY
CATCHER
SPY
CATCHER</div>
    <div class="photo" role="img" aria-label="Colour portrait of the candidate in army camouflage uniform"></div>
    <div class="frame"></div>
    <svg class="tagline" width="346" height="490" aria-label="Spy Catcher">
      <text transform="translate(285 37) rotate(90)" font-size="42" textLength="259" lengthAdjust="spacingAndGlyphs">SPY CATCHER</text>
    </svg>
    <svg class="candidate" viewBox="0 0 280 84" aria-label="Marco"><text x="0" y="84" textLength="280" lengthAdjust="spacingAndGlyphs">MARCO</text></svg>
    <div class="office">CIVITIST FOR CONGRESS</div>
    <div class="web"><span class="web__rule"></span><span class="web__url">www.marcoforhouse.net</span></div>
  </section>

  <section class="flyer flyer--athlete-mono">
    <div class="photo" role="img" aria-label="Black and white photo of the candidate in fencing whites shouting in celebration"></div>
    <div class="frame"></div>
    <svg class="tagline" width="346" height="490" aria-label="Solvanic Athlete">
      <text transform="translate(62 30) rotate(90)" font-size="37" textLength="184" lengthAdjust="spacingAndGlyphs">SOLVANIC</text>
      <text transform="translate(29 30) rotate(90)" font-size="37" textLength="180" lengthAdjust="spacingAndGlyphs">ATHLETE</text>
    </svg>
    <svg class="candidate" viewBox="0 0 280 84" aria-label="Marco"><text x="0" y="84" textLength="280" lengthAdjust="spacingAndGlyphs">MARCO</text></svg>
    <div class="office">CIVITIST FOR CONGRESS</div>
    <div class="web"><span class="web__rule"></span><span class="web__url">www.marcoforhouse.net</span></div>
  </section>

</main>
</body>
</html>
```